Print design needed to improve the layout and look of some existing documents

We need someone to take a couple of existing documents that we have and make them look much better using our existing logo and corporate colors etc. We require these to be delivered in a format that will allow our staff to edit the content as necessary via Microsoft word for conversion once finalized into a PDF. Ideally, we will also be able to use this as a newsletter template or for other documents that might be required in our business. www.calderfinch.com.au
Updates

Project Deadline Extended Reason: So far, I have only seen one design that I believe is quite good quality. Added Sunday, July 3, 2016

Target Market(s)

Business owners, executives, retirees

Industry/Entity Type

Financial Service

Font styles to use
Serif

Requirements
Must have
• Design that uses our existing branding and colors. It also needs to be ina form that we can edit the content / update easily. Ideally the format / layout could also be used for other documents such as short newsletters etc.
Nice to have
• Fresh, simple and crisp. Very professional looking.
Should not have
• strange fonts, weird layouts.

```html
<!DOCTYPE html>
<html lang="en">
<head>
<meta charset="utf-8">
<title>Calder Finch – Financial Service Guide</title>
<link href="https://fonts.googleapis.com/css2?family=Open+Sans:wght@400;600&display=swap" rel="stylesheet">
<style>
  :root{
    --brand-blue:#0a9ad8;
    --brand-green:#7cc242;
    --ink:#333638;
    --frame:#f2f2f4;
    --frame-line:#c9cbce;
    --backdrop:#eceef0;
    --paper:#ffffff;
  }
  html,body{margin:0;padding:0;width:1200px;height:1200px;overflow:hidden;background:var(--backdrop);}
  body{font-family:"Open Sans",Arial,sans-serif;color:var(--ink);}
  .page{position:absolute;left:170px;top:0;width:859px;height:1200px;background:var(--paper);}
  .section-title{position:absolute;left:60px;top:80px;margin:0;font-size:18.5px;font-weight:600;color:var(--brand-blue);letter-spacing:-0.2px;}
  .section-rule{position:absolute;left:60px;top:109px;width:743px;height:2px;background:var(--brand-blue);}
  .intro{position:absolute;left:60px;top:129px;margin:0;font-size:15px;}
  .service-list{position:absolute;left:73px;top:166px;margin:0;padding:0;list-style:none;font-size:15px;}
  .service-list li{height:36.4px;display:flex;align-items:center;}
  .service-list svg{width:12px;height:12px;margin-right:10px;flex:none;}
  .photo-frame{position:absolute;left:65px;top:595px;width:731px;height:392px;background:var(--frame);border:1px solid var(--frame-line);box-shadow:0 14px 10px -8px rgba(0,0,0,.35);}
  .photo{position:absolute;left:16px;top:17px;width:699px;height:360px;
    background:linear-gradient(180deg,#1d6f97 0%,#3d8fb4 16%,#cfe3e6 23%,#b59a86 30%,#8a7f9a 50%,#6f7794 62%,#5f8b4e 78%,#3c5a38 100%);}
  .footer-brand{position:absolute;left:60px;top:1090px;display:flex;align-items:center;gap:8px;}
  .brand-dot{width:14px;height:14px;border-radius:50%;background:var(--brand-blue);}
  .brand-name{font-size:20px;font-weight:400;color:var(--ink);letter-spacing:0.5px;}
  .licence{position:absolute;left:65px;top:1121px;font-size:10px;font-weight:600;}
  .doc-title{position:absolute;right:63px;top:1099px;text-align:right;}
  .doc-title .name{font-size:14px;font-weight:600;color:var(--brand-blue);letter-spacing:0.3px;}
  .doc-title .version{font-size:10.5px;font-weight:600;}
  .footer-rule{position:absolute;left:19px;top:1143px;width:821px;height:3px;background:var(--brand-blue);}
  .footer-rule-thin{position:absolute;left:19px;top:1148px;width:821px;height:1px;background:var(--brand-green);}
</style>
</head>
<body>
<main class="page">
  <h2 class="section-title">WHAT SERVICE DO WE PROVIDE?</h2>
  <div class="section-rule"></div>
  <p class="intro">Calder Finch Pty Ltd holds a licence to provide a comprehensive range of services which includes:</p>
  <ul class="service-list">
    <li><svg viewBox="0 0 12 12"><path d="M6 0 L7.2 4.8 12 6 7.2 7.2 6 12 4.8 7.2 0 6 4.8 4.8Z" fill="#0a9ad8"/></svg>General Superannuation advice</li>
    <li><svg viewBox="0 0 12 12"><path d="M6 0 L7.2 4.8 12 6 7.2 7.2 6 12 4.8 7.2 0 6 4.8 4.8Z" fill="#0a9ad8"/></svg>Self-Managed Superannuation Fund (SMSF) advice</li>
    <li><svg viewBox="0 0 12 12"><path d="M6 0 L7.2 4.8 12 6 7.2 7.2 6 12 4.8 7.2 0 6 4.8 4.8Z" fill="#0a9ad8"/></svg>Securities advice</li>
    <li><svg viewBox="0 0 12 12"><path d="M6 0 L7.2 4.8 12 6 7.2 7.2 6 12 4.8 7.2 0 6 4.8 4.8Z" fill="#0a9ad8"/></svg>Portfolio management and reviews</li>
    <li><svg viewBox="0 0 12 12"><path d="M6 0 L7.2 4.8 12 6 7.2 7.2 6 12 4.8 7.2 0 6 4.8 4.8Z" fill="#0a9ad8"/></svg>Managed Discretionary Account (MDA) services</li>
    <li><svg viewBox="0 0 12 12"><path d="M6 0 L7.2 4.8 12 6 7.2 7.2 6 12 4.8 7.2 0 6 4.8 4.8Z" fill="#0a9ad8"/></svg>Managed investment advice</li>
    <li><svg viewBox="0 0 12 12"><path d="M6 0 L7.2 4.8 12 6 7.2 7.2 6 12 4.8 7.2 0 6 4.8 4.8Z" fill="#0a9ad8"/></svg>Retirement planning advice</li>
    <li><svg viewBox="0 0 12 12"><path d="M6 0 L7.2 4.8 12 6 7.2 7.2 6 12 4.8 7.2 0 6 4.8 4.8Z" fill="#0a9ad8"/></svg>Centrelink &amp; Aged Care Advice</li>
    <li><svg viewBox="0 0 12 12"><path d="M6 0 L7.2 4.8 12 6 7.2 7.2 6 12 4.8 7.2 0 6 4.8 4.8Z" fill="#0a9ad8"/></svg>Personal insurance advice</li>
    <li><svg viewBox="0 0 12 12"><path d="M6 0 L7.2 4.8 12 6 7.2 7.2 6 12 4.8 7.2 0 6 4.8 4.8Z" fill="#0a9ad8"/></svg>Margin lending advice</li>
  </ul>

  <div class="photo-frame">
    <div class="photo" role="img" aria-label="Photograph of a beach at dusk with ocean waves and young plants in green tree guards on the dunes"></div>
  </div>

  <div class="footer-brand">
    <span class="brand-dot"></span>
    <span class="brand-name">CALDER FINCH</span>
  </div>
  <div class="licence">AFSL 000000 | ABN 00 000 000 000</div>
  <div class="doc-title">
    <div class="name">FINANCIAL SERVICE GUIDE</div>
    <div class="version">VERSION 1 - SEPT 2014</div>
  </div>
  <div class="footer-rule"></div>
  <div class="footer-rule-thin"></div>
</main>
</body>
</html>
```